Tallowmere Consulting Group Business Card Design

We have the logo we just need someone to design a modern business card design.

Name: Leopold Ganzhurt
Phone: 3052918364
Mobile: 9178402297
Web:www.tallowmereconsulting.com
email: lganzhurt@tallowmereconsulting.com
Company: Tallowmere Consulting Group
Title: CEO

Address: 718 Quenby Ave, Miami, Florida 33187

Target Market(s)

companies over 100 employees

Industry/Entity Type

Business

```html
<!DOCTYPE html>
<html lang="en">
<head>
<meta charset="utf-8">
<title>Tallowmere Consulting Group – Business Card</title>
<link rel="stylesheet" href="https://fonts.googleapis.com/css2?family=Exo+2:wght@300;400;700&family=Open+Sans:wght@400;700&display=swap">
<style>
  :root {
    --stage: #333333;
    --card-dark: #000000;
    --card-light: #ffffff;
    --brand-blue: #3f63b3;
    --ink: #2b2b2b;
    --ink-soft: #444444;
    --rule: #555555;
    --muted-web: #4a4a4a;
  }
  html, body {
    margin: 0;
    padding: 0;
    width: 900px;
    height: 1200px;
    overflow: hidden;
    background: var(--stage);
  }
  .canvas {
    position: relative;
    width: 900px;
    height: 1200px;
    background: var(--stage);
  }
  .card {
    position: absolute;
    width: 417px;
    height: 232px;
    overflow: hidden;
  }
  .card--front { left: 26px; background: var(--card-dark); }
  .card--back  { left: 458px; background: var(--card-light); }
  .row-1 { top: 120px; }
  .row-2 { top: 459px; }
  .row-3 { top: 801px; }

  /* decorative line-pattern area */
  .pattern {
    position: absolute;
    left: 0; top: 0;
    width: 230px; height: 232px;
  }
  .pattern--blue {
    background: radial-gradient(ellipse at 40% 45%, #16213f 0%, #0b1122 55%, #000 100%);
  }
  .pattern--contrast {
    background: radial-gradient(ellipse at 35% 45%, #2a2f3d 0%, #121826 55%, #000 100%);
  }
  .pattern--muted {
    background: radial-gradient(ellipse at 40% 45%, #1c1c1c 0%, #0e0e0e 60%, #000 100%);
  }

  .brand {
    position: absolute;
    left: 200px;
    top: 56px;
    width: 200px;
    text-align: center;
    font-family: "Open Sans", sans-serif;
    font-weight: 700;
    color: #ffffff;
  }
  .brand__dot {
    display: block;
    width: 72px; height: 72px;
    margin: 0 auto 10px;
    border-radius: 50%;
    background: var(--brand-blue);
  }
  .brand__name {
    display: block;
    font-size: 19px;
    letter-spacing: 0.5px;
    line-height: 1.05;
  }
  .brand__sub {
    display: block;
    font-size: 8.5px;
    letter-spacing: 0.4px;
    line-height: 1.4;
  }
  .website {
    position: absolute;
    left: 220px;
    top: 202px;
    font-family: "Open Sans", sans-serif;
    font-size: 10.5px;
    color: #ffffff;
  }
  .website--muted { color: var(--muted-web); }

  /* back side */
  .holder {
    position: absolute;
    left: 28px;
    top: 100px;
    font-family: "Exo 2", sans-serif;
    font-weight: 300;
    font-size: 23px;
    color: var(--ink);
    letter-spacing: 0.2px;
  }
  .divider {
    position: absolute;
    left: 235px;
    top: 98px;
    width: 1px;
    height: 34px;
    background: var(--rule);
  }
  .role {
    position: absolute;
    left: 248px;
    top: 101px;
    font-family: "Exo 2", sans-serif;
    font-weight: 700;
    font-size: 21px;
    color: var(--ink);
  }
  .role__company {
    position: absolute;
    left: 296px;
    top: 106px;
    font-family: "Open Sans", sans-serif;
    font-size: 5.4px;
    line-height: 1.15;
    color: var(--ink);
  }
  .contacts {
    position: absolute;
    left: 29px;
    top: 171px;
    margin: 0;
    padding: 0;
    list-style: none;
    font-family: "Open Sans", sans-serif;
    font-size: 7.6px;
    line-height: 9.4px;
    color: var(--ink-soft);
  }
  .contacts li {
    display: flex;
    align-items: center;
    gap: 3px;
    white-space: nowrap;
  }
  .contacts b { color: var(--ink); }
  .contacts svg { width: 8px; height: 8px; flex: none; }
</style>
</head>
<body>
<div class="canvas">

  <!-- Row 1 -->
  <section class="card card--front row-1">
    <div class="pattern pattern--blue" role="img" aria-label="Blue outline line pattern decoration"></div>
    <div class="brand">
      <span class="brand__dot"></span>
      <span class="brand__name">TALLOWMERE</span>
      <span class="brand__sub">CONSULTING GROUP</span>
    </div>
    <div class="website">www.tallowmereconsulting.com</div>
  </section>
  <section class="card card--back row-1">
    <div class="holder">Leopold Ganzhurt</div>
    <div class="divider"></div>
    <div class="role">CEO</div>
    <div class="role__company">Tallowmere<br>Consulting<br>Group</div>
    <ul class="contacts">
      <li><svg viewBox="0 0 8 8"><rect width="8" height="8" rx="1.5" fill="#333"/><path d="M2 2.2h1.2l.5 1.2-.7.5c.3.6.6.9 1.1 1.1l.5-.7 1.2.5V6c-2.4 0-3.8-1.4-3.8-3.8z" fill="#fff"/></svg><b>Phone:</b>&nbsp;3052918364</li>
      <li><svg viewBox="0 0 8 8"><rect width="8" height="8" rx="1.5" fill="#333"/><rect x="2.7" y="1.5" width="2.6" height="5" rx=".5" fill="#fff"/></svg><b>Mobile:</b>&nbsp;9178402297</li>
      <li><svg viewBox="0 0 8 8"><rect width="8" height="8" rx="1.5" fill="#333"/><rect x="1.6" y="2.4" width="4.8" height="3.2" fill="#fff"/><path d="M1.6 2.4 4 4.3l2.4-1.9" stroke="#333" stroke-width=".6" fill="none"/></svg><b>eMail:</b>&nbsp;lganzhurt@tallowmereconsulting.com</li>
      <li><svg viewBox="0 0 8 8"><rect width="8" height="8" rx="1.5" fill="#333"/><path d="M4 1.5a1.8 1.8 0 0 1 1.8 1.8C5.8 4.6 4 6.5 4 6.5S2.2 4.6 2.2 3.3A1.8 1.8 0 0 1 4 1.5z" fill="#fff"/></svg><b>Address:</b>&nbsp;718 Quenby Ave, Miami, Florida 33187</li>
    </ul>
  </section>

  <!-- Row 2 -->
  <section class="card card--front row-2">
    <div class="pattern pattern--contrast" role="img" aria-label="Blue and white outline line pattern decoration"></div>
    <div class="brand">
      <span class="brand__dot"></span>
      <span class="brand__name">TALLOWMERE</span>
      <span class="brand__sub">CONSULTING GROUP</span>
    </div>
    <div class="website">www.tallowmereconsulting.com</div>
  </section>
  <section class="card card--back row-2">
    <div class="holder">Leopold Ganzhurt</div>
    <div class="divider"></div>
    <div class="role">CEO</div>
    <div class="role__company">Tallowmere<br>Consulting<br>Group</div>
    <ul class="contacts">
      <li><svg viewBox="0 0 8 8"><rect width="8" height="8" rx="1.5" fill="#333"/><path d="M2 2.2h1.2l.5 1.2-.7.5c.3.6.6.9 1.1 1.1l.5-.7 1.2.5V6c-2.4 0-3.8-1.4-3.8-3.8z" fill="#fff"/></svg><b>Phone:</b>&nbsp;3052918364</li>
      <li><svg viewBox="0 0 8 8"><rect width="8" height="8" rx="1.5" fill="#333"/><rect x="2.7" y="1.5" width="2.6" height="5" rx=".5" fill="#fff"/></svg><b>Mobile:</b>&nbsp;9178402297</li>
      <li><svg viewBox="0 0 8 8"><rect width="8" height="8" rx="1.5" fill="#333"/><rect x="1.6" y="2.4" width="4.8" height="3.2" fill="#fff"/><path d="M1.6 2.4 4 4.3l2.4-1.9" stroke="#333" stroke-width=".6" fill="none"/></svg><b>eMail:</b>&nbsp;lganzhurt@tallowmereconsulting.com</li>
      <li><svg viewBox="0 0 8 8"><rect width="8" height="8" rx="1.5" fill="#333"/><path d="M4 1.5a1.8 1.8 0 0 1 1.8 1.8C5.8 4.6 4 6.5 4 6.5S2.2 4.6 2.2 3.3A1.8 1.8 0 0 1 4 1.5z" fill="#fff"/></svg><b>Address:</b>&nbsp;718 Quenby Ave, Miami, Florida 33187</li>
    </ul>
  </section>

  <!-- Row 3 -->
  <section class="card card--front row-3">
    <div class="pattern pattern--muted" role="img" aria-label="Faint grey outline line pattern decoration"></div>
    <div class="brand">
      <span class="brand__dot"></span>
      <span class="brand__name">TALLOWMERE</span>
      <span class="brand__sub">CONSULTING GROUP</span>
    </div>
    <div class="website website--muted">www.tallowmereconsulting.com</div>
  </section>
  <section class="card card--back row-3">
    <div class="holder">Leopold Ganzhurt</div>
    <div class="divider"></div>
    <div class="role">CEO</div>
    <div class="role__company">Tallowmere<br>Consulting<br>Group</div>
    <ul class="contacts">
      <li><svg viewBox="0 0 8 8"><rect width="8" height="8" rx="1.5" fill="#333"/><path d="M2 2.2h1.2l.5 1.2-.7.5c.3.6.6.9 1.1 1.1l.5-.7 1.2.5V6c-2.4 0-3.8-1.4-3.8-3.8z" fill="#fff"/></svg><b>Phone:</b>&nbsp;3052918364</li>
      <li><svg viewBox="0 0 8 8"><rect width="8" height="8" rx="1.5" fill="#333"/><rect x="2.7" y="1.5" width="2.6" height="5" rx=".5" fill="#fff"/></svg><b>Mobile:</b>&nbsp;9178402297</li>
      <li><svg viewBox="0 0 8 8"><rect width="8" height="8" rx="1.5" fill="#333"/><rect x="1.6" y="2.4" width="4.8" height="3.2" fill="#fff"/><path d="M1.6 2.4 4 4.3l2.4-1.9" stroke="#333" stroke-width=".6" fill="none"/></svg><b>eMail:</b>&nbsp;lganzhurt@tallowmereconsulting.com</li>
      <li><svg viewBox="0 0 8 8"><rect width="8" height="8" rx="1.5" fill="#333"/><path d="M4 1.5a1.8 1.8 0 0 1 1.8 1.8C5.8 4.6 4 6.5 4 6.5S2.2 4.6 2.2 3.3A1.8 1.8 0 0 1 4 1.5z" fill="#fff"/></svg><b>Address:</b>&nbsp;718 Quenby Ave, Miami, Florida 33187</li>
    </ul>
  </section>

</div>
</body>
</html>
```